依頼詳細
企画内容や入れた欲しい文言は添付資料にあります。(A4で2枚分)
文字の大きさや赤字は私が強調したいと考えているイメージと捉えてください。
また、文言・キャッチ等の変更の提案は大歓迎です。是非勉強させてください!

イメージしている事
・女性がターゲットになっているような雰囲気。
・当たり障りのないというよりは、どこか振り切れているような個性的な雰囲気。
・「頑張ってやってくれそうね。」という印象を持ってもらいたい。
今回ワークテラスさんに依頼するのは、2回目ですが前回(下敷きのデザイン)は、ワークテラスさんの色々な提案により当初イメージしていたものよりいい物ができたので、色々な提案や質問は大歓迎です。

また、出来れば今回の依頼の中で、今後も定期的にデザインをお願いできる方がいればという事を兼ねているので、定期的に(大体「月1」位のペース)お願いできる方はその旨お伝えください。

私が選考するポイント
・キャッチやレイアウト等、ターゲットからのレスポンスがありそうか?
私はチラシは如何にして見て読んだ瞬間にアクション(問い合わせ)を起こさせるかがポイントだと思っています。
・レスポンスの速さ(私は速くないですが)等の対応
記載項目
屋号:学習塾 ミナリオ
電話番号:047-513-8847
URL:http://minario-juku.jp/
※ 二次元コードとロゴは添付資料よりおとりください。
サイズ
B4
ページ数
両面
希望イメージ
シンプル 複雑
単色 カラフル
暗い 明るい
日常 高級
遊び心 厳粛
未来的 伝統的
女性的 男性的
希望する色
大きな希望はないですが、塾のイメージはオレンジです。
納品ファイル
• 高解像度JPG (.jpg)
• イラストレーター形式 (.ai)
• フォトショップ形式 (.psd)
補足説明
今回のチラシでは、塾長をある程度前面に出した形にしようと思っているので、
「ここにこんなポーズの写真をいれましょう!」
などのご提案も受け付けます。
言っていただければ、はめ込みもしやすいように白バックで撮ってお渡しします。

また、チラシの依頼は初めてなので説明の足りない箇所等あると思いますので、
その際はお手数ですが、ご質問ください。
キャンペーン面の下部に
「HPに『無料体験者の感想』を掲載しています」
とHPに誘導する仕組みを作成してください。
塾長の写真をアップしました。
ご確認ください。
たくさんのご提案ありがとうございました。
依頼の段階でもお伝えした通り、できれば今後も定期的にお願いできる方が希望です。
定期的な依頼が可能なのに、その旨お伝えいただいていない方はメッセージ等で、その旨ご連絡ください。

選定段階(修正依頼等)に入りましたら、またこの欄にてご報告させていただきます。
(少なくとも金曜日までにはアクションをおこします。)

本当にたくさんのご提案ありがとうございました。
■ 選んだ理由

私の当初のイメージ(熱意がありそう・ちゃんとした塾でありそう)
に、一番近かった事が最大の決め手でした。
また、私が添付したデータはただ腕組みをしている写真でしたが、
動きのある写真の方がいいなぁと、漠然には感じていた所も大きいかと思います。

■ 提案者全員のお礼・コメント

この度は、弊社の依頼にご提案いただき誠にありがとうございました。
正直、選考するのにかなり悩みました。
私が、原案の中で気になっていた箇所をうまくまとめていただいた方、
文言の言い回しの修正の仕方など、とても勉強になりました。
また、依頼をさせていただく際には、是非ご提案いただければと思います。

```html
<!DOCTYPE html>
<html lang="ja">
<head>
<meta charset="utf-8">
<title>中間テスト20点UP保証 学習塾 ミナリオ</title>
<link href="https://fonts.googleapis.com/css2?family=Dela+Gothic+One&family=Noto+Sans+JP:wght@400;700;900&display=swap" rel="stylesheet">
<style>
:root{
  --orange:#f08a00;
  --orange-light:#fbd08a;
  --orange-pale:#fdf0dc;
  --red:#e0201b;
  --ink:#1c1c1c;
  --grey:#777;
  --white:#fff;
}
*{margin:0;padding:0;box-sizing:border-box}
html,body{width:856px;height:1200px;overflow:hidden;background:var(--white)}
body{font-family:"Noto Sans JP",sans-serif;color:var(--ink);position:relative}
.abs{position:absolute}
.hero-band{left:0;top:0;width:856px;height:170px;background:var(--orange)}
.hero-title{left:30px;top:14px;color:var(--white);font-family:"Dela Gothic One",sans-serif;font-size:70px;line-height:78px;letter-spacing:2px;text-shadow:3px 3px 0 rgba(0,0,0,.15)}
.hero-guarantee{left:560px;top:56px;color:var(--white);font-family:"Dela Gothic One",sans-serif;font-size:84px;line-height:90px;text-shadow:3px 3px 0 rgba(0,0,0,.15)}
.up-arrow{left:452px;top:46px}
.refund-note{left:34px;top:176px;font-size:17px;font-weight:700;color:var(--grey)}
.refund-note b{color:var(--red);font-size:20px}
.subcatch{left:36px;top:220px;font-size:32px;font-weight:900;color:var(--orange);font-style:italic;letter-spacing:1px}
.maincatch{left:36px;top:262px;font-family:"Dela Gothic One",sans-serif;font-size:60px;color:var(--ink);font-weight:400}
.maincatch .em{color:var(--red)}
.side-shout{left:752px;top:180px;writing-mode:vertical-rl;font-size:26px;font-weight:900;color:var(--red);line-height:36px;letter-spacing:2px}
.director-photo{left:470px;top:330px;width:280px;height:520px;background:linear-gradient(180deg,#d9d4cf,#8b8680 70%,#3b3b3b)}
.lead{left:150px;top:356px;font-size:22px;font-weight:900;text-align:right;line-height:30px}
.lead .red{color:var(--red)}
.course-name{left:60px;top:424px;width:380px;height:92px;background:linear-gradient(90deg,#2a2a2a,#555)}
.side-panel{left:20px;top:524px;width:70px;height:208px;background:var(--orange);color:var(--white);writing-mode:vertical-rl;font-size:13px;font-weight:700;padding:8px;line-height:18px}
.total{left:110px;top:526px;text-align:center;width:350px}
.total .small{font-size:16px;font-weight:700}
.total .big{font-size:32px;font-weight:900;color:var(--red);white-space:nowrap}
.schedule{left:110px;top:600px;width:350px;border-collapse:collapse;font-size:11px}
.schedule td{border:1px solid var(--orange);padding:3px 5px;height:22px}
.schedule td:first-child{background:var(--orange-pale);width:70px;font-weight:700}
.bonus-badge{left:20px;top:744px;width:70px;height:70px;border-radius:50%;background:var(--red);color:var(--white);font-size:14px;font-weight:900;text-align:center;padding-top:14px;line-height:20px}
.bonus-text{left:104px;top:748px;width:350px;font-size:17px;font-weight:900;line-height:26px}
.bonus-text .red{color:var(--red)}
.info{left:20px;top:820px;width:440px;border-collapse:collapse;font-size:13px;line-height:18px}
.info td{border:1px solid #bbb;padding:3px 8px;height:24px}
.info td:first-child{background:var(--orange-pale);width:70px;font-weight:700;text-align:center}
.contact-label{left:20px;top:934px;width:56px;height:96px;background:var(--orange);color:var(--white);writing-mode:vertical-rl;font-size:14px;font-weight:700;padding:10px 14px}
.contact{top:934px;height:96px;border:2px solid var(--orange);padding:8px 4px;text-align:center}
.contact .ttl{font-size:13px;font-weight:700;color:var(--orange)}
.contact .val{font-size:14px;font-weight:900;margin-top:22px;white-space:nowrap}
.nameplate{left:600px;top:800px;background:var(--white);padding:4px 10px;font-size:13px;font-weight:700}
.nameplate b{font-size:22px}
.voices{left:560px;top:946px;width:270px;border:2px solid var(--orange);padding:8px;font-size:13px;font-weight:700;line-height:20px}
.voices .red{color:var(--red)}
.footer-line{left:0;top:1046px;width:856px;height:6px;background:var(--orange)}
.brand{left:20px;top:1066px;width:220px;text-align:center}
.brand .name{font-size:40px;font-weight:900;color:var(--orange);display:flex;align-items:center;justify-content:center;gap:8px}
.brand .dot{width:20px;height:20px;background:var(--orange);border-radius:50%}
.brand .tag{margin-top:6px;background:var(--orange);color:var(--white);font-size:16px;font-weight:700;padding:3px}
.recruit{left:262px;top:1058px;font-family:"Dela Gothic One",sans-serif;font-size:50px;color:var(--orange)}
.phone-big{left:262px;top:1126px;font-family:"Dela Gothic One",sans-serif;font-size:40px;color:var(--orange);white-space:nowrap}
.hours{left:700px;top:1136px;font-size:12px;font-weight:700;line-height:16px}
.consult{left:680px;top:1074px;background:var(--red);color:var(--white);font-size:14px;font-weight:700;padding:6px 12px;border-radius:4px}
.url{left:262px;top:1180px;font-size:12px;color:var(--grey)}
</style>
</head>
<body>
<div class="abs hero-band"></div>
<div class="abs hero-title">中間テスト<br>20点UP</div>
<svg class="abs up-arrow" width="90" height="110" viewBox="0 0 90 110"><path d="M45 0 L90 50 L62 50 L62 110 L28 110 L28 50 L0 50 Z" fill="#fff"/></svg>
<div class="abs hero-guarantee">保証!!</div>
<p class="abs refund-note">上がらなかったら<b>授業料は全額お返しして、補習授業を行います</b></p>
<p class="abs subcatch">定期テスト対策塾がみせる</p>
<h1 class="abs maincatch">本物の<span class="em">指導力!</span></h1>
<p class="abs side-shout">数学嫌いな若者よ<br>いつまでも逃げちゃダメだ!</p>

<div class="abs director-photo" role="img" aria-label="塾長が親指を立てて前に手を伸ばす写真"></div>

<p class="abs lead"><span class="red">塾長が直接指導!</span><br>中間テスト短期特訓講座!</p>
<div class="abs course-name" role="img" aria-label="筆文字のロゴ「中間特講 塾長直伝」"></div>

<div class="abs side-panel">定期テスト前の短期集中講座で苦手を克服します</div>
<div class="abs total"><p class="small">個別指導+直前試験対策授業</p><p class="big">合計720分徹底指導!</p></div>
<table class="abs schedule">
<tr><td>1週目</td><td>個別指導 90分×2回 苦手単元の確認</td></tr>
<tr><td>2週目</td><td>個別指導 90分×2回 演習と解説</td></tr>
<tr><td>3週目</td><td>直前対策 120分×1回 予想問題演習</td></tr>
<tr><td>前日</td><td>直前対策 120分×1回 総仕上げ</td></tr>
<tr><td>合計</td><td>720分</td></tr>
</table>

<div class="abs bonus-badge">さらに<br>超特典</div>
<p class="abs bonus-text">見直し授業として<br><span class="red">60分の個別指導を2回無料</span>で行います!</p>

<table class="abs info">
<tr><td>期間</td><td>各中学の定期テストまでの短期特訓</td></tr>
<tr><td>受講料</td><td>10,000円(税込)</td></tr>
<tr><td>定員</td><td>10名</td></tr>
<tr><td>締切</td><td>5月13日(月)</td></tr>
</table>

<div class="abs contact-label">お申し込み</div>
<div class="abs contact" style="left:80px;width:118px"><p class="ttl">電話</p><p class="val">047-513-8847</p></div>
<div class="abs contact" style="left:202px;width:150px"><p class="ttl">メール</p><p class="val" style="font-size:10px">http://minario-juku.jp/</p></div>
<div class="abs contact" style="left:356px;width:104px"><p class="ttl">FAX</p><p class="val" style="font-size:13px">047-513-8850</p></div>

<p class="abs nameplate">塾長 <b>森川 健介</b></p>
<div class="abs voices">HPに<span class="red">「通塾生・保護者の声」</span>掲載中!<br>http://minario-juku.jp/</div>

<div class="abs footer-line"></div>
<div class="abs brand"><p class="name"><span class="dot"></span>ミナリオ</p><p class="tag">完全個別指導</p></div>
<p class="abs recruit">新規生徒募集中!!</p>
<p class="abs consult">お気軽にご相談下さい</p>
<p class="abs phone-big">047-513-8847</p>
<p class="abs hours">受付時間<br>10:00~22:00</p>
<p class="abs url">http://minario-juku.jp/</p>
</body>
</html>
```